Consulting Company needs business card design

We need a business card design for a new consulting and business solutions company based in Bermuda called Corvale Partners Limited. Looking for a double sided business card with one side only including the company logo thats attached and the other including contact information. Logo contains blue and turquoise colors and is fine to be on both sides of the card.
Contact Information for Business Card
Corvale Partners Limited
P.O. Box HM318
Devonshire DV BX
Bermuda
Name: Marcus Pellegrin
Position: Director
Telephone: 1 441 733 4906
Email: mpellegrin@corvale.example
Website: www.corvale.example

```html
<!DOCTYPE html>
<html lang="en">
<head>
<meta charset="utf-8">
<title>Corvale Partners Limited – Business Card</title>
<link href="https://fonts.googleapis.com/css2?family=Questrial&display=swap" rel="stylesheet">
<style>
  :root {
    --backdrop: #4b4b4b;
    --card: #121212;
    --blue: #27a8e3;
    --turquoise: #1fb8b0;
    --white: #f2f2f2;
    --muted: #cfcfcf;
  }
  * { box-sizing: border-box; margin: 0; padding: 0; }
  html, body { width: 1200px; height: 799px; overflow: hidden; }
  body {
    background: var(--backdrop);
    font-family: "Questrial", "Century Gothic", sans-serif;
    display: flex;
    flex-direction: column;
    align-items: center;
    justify-content: center;
    gap: 56px;
  }
  .card {
    position: relative;
    width: 540px;
    height: 308px;
    background: var(--card);
    box-shadow: 0 10px 28px rgba(0,0,0,.45);
    overflow: hidden;
  }
  .band { position: absolute; left: 0; right: 0; height: 8px; background: var(--blue); }
  .band--top { top: 0; }
  .band--bottom { bottom: 0; }

  /* Front */
  .brand {
    position: absolute; inset: 0;
    display: flex; align-items: center; justify-content: center; gap: 14px;
  }
  .brand__dot { width: 40px; height: 40px; border-radius: 50%; background: var(--blue); }
  .brand__name {
    color: var(--blue);
    font-size: 26px;
    letter-spacing: 2px;
    text-transform: uppercase;
  }

  /* Back */
  .person {
    position: absolute; left: 70px; top: 112px; width: 215px; text-align: right;
  }
  .person__name { font-size: 21px; letter-spacing: .5px; text-transform: uppercase; }
  .person__first { color: var(--blue); }
  .person__last { color: var(--white); }
  .person__role { color: var(--muted); font-size: 15px; margin-top: 2px; }
  .divider {
    position: absolute; left: 306px; top: 96px; width: 2px; height: 82px;
    background: linear-gradient(transparent, var(--blue), transparent);
  }
  .contacts {
    position: absolute; left: 326px; top: 98px; list-style: none;
    color: var(--white); font-size: 12.5px; letter-spacing: .4px;
  }
  .contacts li { display: flex; align-items: center; gap: 10px; height: 26px; }
  .contacts svg { width: 14px; height: 14px; flex: none; }
  .address {
    position: absolute; left: 0; right: 0; bottom: 26px;
    display: flex; justify-content: center; align-items: center; gap: 10px;
    color: var(--white); font-size: 12px; letter-spacing: .5px;
  }
  .address__flag { width: 22px; height: 13px; background: #c8202f; }
</style>
</head>
<body>
  <section class="card card--front">
    <div class="band band--top"></div>
    <div class="brand">
      <span class="brand__dot"></span>
      <span class="brand__name">Corvale Partners Limited</span>
    </div>
    <div class="band band--bottom"></div>
  </section>

  <section class="card card--back">
    <div class="person">
      <p class="person__name"><span class="person__first">Marcus</span> <span class="person__last">Pellegrin</span></p>
      <p class="person__role">Director</p>
    </div>
    <div class="divider"></div>
    <ul class="contacts">
      <li>
        <svg viewBox="0 0 24 24" fill="var(--blue)"><path d="M6.6 10.8a15.1 15.1 0 0 0 6.6 6.6l2.2-2.2a1 1 0 0 1 1-.25 11.4 11.4 0 0 0 3.6.57 1 1 0 0 1 1 1V20a1 1 0 0 1-1 1A17 17 0 0 1 3 4a1 1 0 0 1 1-1h3.5a1 1 0 0 1 1 1c0 1.25.2 2.45.57 3.57a1 1 0 0 1-.25 1z"/></svg>
        <span>1 441 733 4906</span>
      </li>
      <li>
        <svg viewBox="0 0 24 24" fill="none" stroke="var(--blue)" stroke-width="2"><rect x="3" y="5" width="18" height="14"/><path d="M3 5l9 8 9-8"/></svg>
        <span>mpellegrin@corvale.example</span>
      </li>
      <li>
        <svg viewBox="0 0 24 24" fill="none" stroke="var(--blue)" stroke-width="2"><circle cx="12" cy="12" r="9"/><path d="M3 12h18M12 3c3 3 3 15 0 18M12 3c-3 3-3 15 0 18"/></svg>
        <span>www.corvale.example</span>
      </li>
    </ul>
    <p class="address">
      <span class="address__flag" role="img" aria-label="Flag of Bermuda"></span>
      <span>P.O. Box HM318, Devonshire DV BX, Bermuda</span>
    </p>
    <div class="band band--bottom"></div>
  </section>
</body>
</html>
```